Event Listing Website

We need a redesign of a site for a new startup that lists local events such as concerts, night clubs, stand up comedy shows, theater plays, festivals, conferences, seminars, and family events.

The original design was done by programmers, not designers, and thus can be greatly improved, especially in terms of flow and usability.

The current site can be viewed at:
http://projects.brinvexsystems.example/pellora/index.php/events/

The successful designer may also be hired for additional work. In fact, we are looking for a long-time partner that may eventually fill a Creative Director role with this new venture..

Things to note:

The site should not look like a nightlife/disco/club site since the site lists events from concerts to conferences to family events.

There is a lot of content on the site, thus it needs to be clean, easy to read and navigate.

Our mission is to have a “Unique” site, that stands out from the traditional ones

Currently the site has these main sections:

Homepage
Events
Venues
Cinema

These sections have the following content types or page layouts:

Homepage
Listing of events
Listing of venues
Event details
Venue details
Cinema summary page
Film details
Film theater details
Blog/news
Account overview page
Updates

Please note, an important element of the site is the location picker that is currently on the top left of our site (the black drop down button that says "change", enter Roma for example). The site displays events based on user location, users need to know what city the site is using and need to be able to change such city. This works similar to many sites such as www.dealnorva.example, www.partyvesk.example, and www.happenlo.example.

Also, please note that we would eventually use background ads on the homepage. See www.ticketmurn.example for example.

I have extended the project further. Thanks!

Please note, after the main menu (Home, Events, Venues, Cinema) these pages or features are very important and should be visible and prominent. We currently have them on a bar across the top that remains fixed as you scroll down, but it may not be the best location, so we look forward to some fresh ideas. Thanks.

In order of importance:

1. Change your location (Button that says current city with option to change it)
2. Add event (link)
3. Add venue (link)
4. Login (link)
5. Change language (drop down button with languages)

I just increased the budget by $40 :)

When submitting a design, please submit two versions, one with background advertisement, and one without. This way we can see if there are too many colors or distractions.

Here is a sample background advertisement to use: http://lentobanner.example/img_uploads/72/77_191072_3_Korvex_Viola_Tab_Adriva_newsln_skin2.jpg

Hello all, thanks for submitting your beautiful designs. It has made our decision very difficult. We decided to award to project to Merostin, who is currently working on making some tweaks to his submission. Thus are no longer accepting designs. Thanks again.

Target Market(s)

17-40 year olds, male and female, clubbers, concert goers, professionals, athletes, families, and kids

Industry/Entity Type

Events

Requirements
Must have
• Needs to follow 960 grid system. See http://gridlane.example.
Nice to have
• We like the colors Bravik Nearby
(http://nearby.bravik.example/westside-south-bay)

We like Dealnorva theme as well
(http://www.dealnorva.example/los-angeles/)

Happenlo is a site similar to ours, we like the overall layout and how easy it is to navigate, not necessarily the colors though:
(http://happenlo.example/)
Should not have
• The site should not look like a nightlife/disco/club site.

Besides clubs, the site lists events from concerts to conferences to family events.

Should definitely not use serif fonts such as Times New Roman

```html
<!DOCTYPE html>
<html lang="it">
<head>
<meta charset="utf-8">
<title>Pellora – Eventi</title>
<link href="https://fonts.googleapis.com/css2?family=Arimo:wght@400;700&display=swap" rel="stylesheet">
<style>
:root{
  --canvas:#e6e6e6;
  --page:#ffffff;
  --panel:#f4f4f4;
  --line:#d2d2d2;
  --ink:#333333;
  --muted:#777777;
  --blue:#3f73a6;
  --blue-dark:#2d5a87;
  --blue-text:#2f66a0;
  --orange:#f07d1a;
  --dark:#333333;
  --darker:#2a2a2a;
  --footer-text:#bdbdbd;
  --venue-light:#7fb35e;
  --venue-dark:#3f7d2e;
}
*{box-sizing:border-box;margin:0;padding:0}
html,body{width:730px;height:1200px;overflow:hidden}
body{background:var(--canvas);font-family:"Arimo",Arial,sans-serif;color:var(--ink);position:relative;font-size:8px;line-height:1.25}
.abs{position:absolute}
.ad-band{left:115px;top:0;width:500px;height:72px;background:var(--dark);color:#777;font-size:17px;display:flex;align-items:center;justify-content:center}
.page{left:115px;top:82px;width:500px;height:1103px;background:var(--page);border:1px solid var(--line)}
.header{left:0;top:0;width:498px;height:62px;background:#fafafa;border-bottom:1px solid var(--line)}
.brand{left:28px;top:14px;font-size:30px;font-weight:700;color:var(--ink)}
.edition{left:172px;top:22px;font-size:8px;display:flex;align-items:center;gap:6px}
.dropdown{display:inline-flex;align-items:center;justify-content:space-between;height:13px;padding:0 4px;font-size:8px}
.dropdown.city{width:62px;background:var(--orange);color:#fff}
.dropdown.lang{width:80px;background:#fff;border:1px solid #aaa;color:var(--ink)}
.caret{width:0;height:0;border-left:3px solid transparent;border-right:3px solid transparent;border-top:4px solid currentColor}
.divider{left:318px;top:8px;width:1px;height:46px;background:var(--line)}
.top-links{left:365px;top:8px;display:flex;gap:10px;font-size:8px}
.social{left:335px;top:22px;display:flex;gap:3px}
.social span{width:11px;height:11px;background:#8aa9c8;display:block}
.lang-pos{left:412px;top:22px}
.search{left:322px;top:40px;display:flex;gap:6px}
.search .field{width:88px;height:12px;border:1px solid #aaa;background:#fff;font-size:7px;padding:1px 3px}
.btn-orange{background:var(--orange);color:#fff;font-size:8px;display:inline-flex;align-items:center;justify-content:center}
.search .btn-orange{width:42px;height:12px}
.nav{left:0;top:63px;width:498px;height:16px;background:linear-gradient(#5a8dbd,var(--blue));display:flex}
.nav a{color:#fff;text-decoration:none;font-size:8px;padding:0 10px;display:flex;align-items:center;border-right:1px solid #6e9cc8}
.nav a.active{background:var(--blue-dark)}
.box{background:var(--page);border:1px solid var(--line);border-radius:3px}
.box-title{color:var(--blue-text);font-size:10px;font-weight:700;padding:5px 8px}
.expand{position:absolute;right:8px;top:6px;font-size:7px;display:flex;align-items:center;gap:2px}
.expand i{width:7px;height:7px;border:1px solid #888;display:block}
.bar-title{background:linear-gradient(#4f83b5,var(--blue));color:#fff;font-weight:700;font-size:10px;padding:5px 8px}
.arrow{position:absolute;width:14px;height:34px;background:#f1f1f1;border:1px solid #ccc;display:flex;align-items:center;justify-content:center}
.arrow svg{width:6px;height:9px}
.event-name{left:122px;width:140px;height:13px;background:#e9e9e9;color:var(--blue-text);font-weight:700;font-size:9px;padding:2px 6px}
.event-meta{left:122px;font-size:7px;line-height:1.3}
.event-meta b{font-weight:700}
.calendar{left:8px;top:24px;width:72px;height:58px;border:1px solid var(--blue)}
.cal-month{background:var(--blue);color:#fff;text-align:center;font-size:7px;height:11px;line-height:11px}
.cal-day{text-align:center;font-size:24px;font-weight:700;height:36px;line-height:36px;color:var(--ink)}
.cal-week{background:var(--blue);color:#fff;text-align:center;font-size:7px;height:10px;line-height:10px}
.link-list{list-style:none;color:var(--blue-text);font-size:6.5px;line-height:1.25;white-space:nowrap}
.mini-nav{left:244px;top:44px;width:40px;height:10px;display:flex;justify-content:space-between;align-items:center;border:1px solid #ccc;padding:0 4px}
.cat-grid{left:10px;top:24px;display:grid;grid-template-columns:repeat(6,46px);font-size:6.5px;color:var(--blue-text);line-height:1.2}
.thumbs{top:30px;display:flex;gap:6px}
.thumb{width:55px;text-align:center;font-size:6.5px;line-height:1.2}
.thumb .frame{width:46px;height:46px;margin:0 auto 5px;border:3px solid #fff;box-shadow:0 0 0 1px #ccc,0 2px 3px rgba(0,0,0,.25)}
.tone-event{background:linear-gradient(#6b5a4e,#bfa07d)}
.tone-cinema{background:linear-gradient(#5e4a34,#c79a52)}
.tone-venue{background:linear-gradient(160deg,var(--venue-light),var(--venue-dark))}
.subscribe{left:126px;width:296px;height:60px;background:var(--blue);border-radius:3px}
.subscribe h3{color:#fff;font-size:11px;padding:7px 8px}
.subscribe .field{position:absolute;left:8px;top:30px;width:224px;height:14px;background:#fff}
.subscribe .btn-orange{position:absolute;left:240px;top:30px;width:46px;height:14px}
.map-area{left:6px;top:6px;width:160px;height:138px;background:linear-gradient(135deg,#a9c3de,#cfd9c4 45%,#e4e0cc 60%,#a9c3de)}
.map-tabs{left:60px;top:8px;display:flex;font-size:6px}
.map-tabs span{background:#fff;border:1px solid #999;padding:1px 4px}
.btn-large-map{left:92px;top:138px;width:66px;height:12px}
.feed-inner{left:6px;top:18px;width:160px;border:1px solid #ccc;background:#fff}
.post{display:flex;gap:5px;padding:5px;font-size:6px;line-height:1.25;color:#555}
.post .avatar{width:20px;height:20px;background:#d9d9d9;flex:none}
.post b{color:var(--blue-text);font-size:7px;display:block}
.fans{display:flex;gap:6px;padding:0 5px;font-size:5.5px;text-align:center;color:#555}
.fans .face{width:22px;height:22px;background:#cfcfcf;margin-bottom:2px}
.news-head{background:#e0e0e0;font-size:10px;font-weight:700;padding:5px 8px}
.news-item{padding:5px 8px;border-bottom:1px solid #ddd;font-size:6.5px;line-height:1.3}
.news-item:nth-child(even){background:#f4f4f4}
.news-date{color:var(--orange)}
.footer{left:115px;top:1020px;width:500px;height:165px;background:var(--darker)}
.footer-nav{left:0;top:12px;width:500px;display:flex;justify-content:space-around;color:#fff;font-size:8px;font-weight:700}
.footer-sub{left:215px;top:52px;color:var(--footer-text);font-size:7px;line-height:1.3;list-style:none}
.footer-rule{left:20px;top:132px;width:460px;height:1px;background:#444}
.copyright{left:0;top:142px;width:500px;text-align:center;color:var(--footer-text);font-size:7px}
</style>
</head>
<body>

<div class="abs ad-band">960X120 Ads</div>

<div class="abs page">
  <header class="abs header">
    <div class="abs brand">Pellora</div>
    <div class="abs edition">Your Edition <span class="dropdown city">Roma <i class="caret"></i></span></div>
    <div class="abs divider"></div>
    <nav class="abs top-links"><span>Login</span><span>Add Location</span><span>Add Venue</span></nav>
    <div class="abs social"><span></span><span></span><span></span><span></span></div>
    <div class="abs lang-pos"><span class="dropdown lang">Italian <i class="caret"></i></span></div>
    <div class="abs search"><div class="field">Keywords</div><div class="btn-orange">Search</div></div>
  </header>
  <nav class="abs nav"><a class="active">Home</a><a>Event</a><a>Venues</a><a>Cinema</a></nav>
</div>

<section class="abs box" style="left:126px;top:183px;width:296px;height:155px">
  <div class="bar-title">Eventi In Prima Fila</div>
  <div class="arrow" style="left:8px;top:60px"><svg viewBox="0 0 6 9"><path d="M5 0L0 4.5 5 9z" fill="#555"/></svg></div>
  <div class="arrow" style="right:8px;top:60px"><svg viewBox="0 0 6 9"><path d="M1 0l5 4.5L1 9z" fill="#555"/></svg></div>
  <div class="abs" role="img" aria-label="Foto del protagonista dell'evento" style="left:36px;top:42px;width:70px;height:82px;background:linear-gradient(135deg,#7d6650,#c6a98a 55%,#5e4f43)"></div>
  <div class="abs event-name" style="top:46px">Marco Velluti</div>
  <div class="abs event-meta" style="top:64px">
    <b>Quando</b><br>2012 - 03 - 04<br><b>Dove</b><br>Piazza Lunetta 12, MILANO, Italia, 20100<br>MILANO<br>Italia<br>20100
  </div>
  <div class="abs btn-orange" style="left:122px;top:136px;width:50px;height:13px">Buy Tickets</div>
</section>

<section class="abs box" style="left:126px;top:348px;width:296px;height:90px">
  <div class="box-title">Filtra Per Data</div>
  <div class="expand"><i></i>Expand</div>
  <div class="abs calendar"><div class="cal-month">March</div><div class="cal-day">02</div><div class="cal-week">Friday</div></div>
  <ul class="abs link-list" style="left:92px;top:24px"><li>Questo Weekend</li><li>Prossimo Weekend</li><li>Questa Settimana</li><li>Prossima Settimana</li><li>Questo Mese</li><li>Prossimo Mese</li><li>Eventi Passati</li></ul>
  <ul class="abs link-list" style="left:168px;top:24px"><li>Questo Weekend</li><li>Prossimo Weekend</li><li>Questa Settimana</li><li>Prossima Settimana</li><li>Questo Mese</li><li>Prossimo Mese</li><li>Eventi Passati</li></ul>
  <div class="abs mini-nav"><svg width="4" height="6" viewBox="0 0 6 9"><path d="M5 0L0 4.5 5 9z" fill="#555"/></svg><svg width="4" height="6" viewBox="0 0 6 9"><path d="M1 0l5 4.5L1 9z" fill="#555"/></svg></div>
</section>

<section class="abs box" style="left:126px;top:447px;width:296px;height:93px">
  <div class="box-title">Filtra Per Catagoria</div>
  <div class="expand"><i></i>Expand</div>
  <div class="abs cat-grid">
    <span>Food</span><span>Musica</span><span>Altrostesso</span><span>Musica</span><span>Altrostesso</span><span>Altrostesso</span>
    <span>Family</span><span>Internazionale</span><span>Altrostesso</span><span>Altrostesso</span><span>Altrostesso</span><span>Altrostesso</span>
    <span>Conferenze</span><span>Teatro</span><span>Dance</span><span>Dance</span><span>Dance</span><span>Dance</span>
    <span>Festivals</span><span>Football</span><span>Play</span><span>Play</span><span>Play</span><span>Play</span>
    <span>Concerts</span><span>Opera</span><span>Opera</span><span>Opera</span><span>Opera</span><span>Opera</span>
    <span>Nightlife</span><span>Dance</span><span>Musica</span><span>Musica</span><span>Musica</span><span>Musica</span>
    <span>Bar</span><span>Usa - che</span><span>Italiana</span><span>Italiana</span><span>Italiana</span><span>Italiana</span>
  </div>
</section>

<section class="abs box" style="left:126px;top:549px;width:296px;height:116px">
  <div class="box-title">Event Lorem Ipsum Dolor Sit Amet</div>
  <div class="arrow" style="left:8px;top:40px"><svg viewBox="0 0 6 9"><path d="M5 0L0 4.5 5 9z" fill="#555"/></svg></div>
  <div class="arrow" style="right:8px;top:40px"><svg viewBox="0 0 6 9"><path d="M1 0l5 4.5L1 9z" fill="#555"/></svg></div>
  <div class="abs thumbs" style="left:36px">
    <div class="thumb"><div class="frame tone-event" role="img" aria-label="Immagine evento"></div>Lorem ipsum<br>dolor sit amet</div>
    <div class="thumb"><div class="frame tone-event" role="img" aria-label="Immagine evento"></div>Lorem ipsum<br>dolor sit amet</div>
    <div class="thumb"><div class="frame tone-event" role="img" aria-label="Immagine evento"></div>Lorem ipsum<br>dolor sit amet</div>
    <div class="thumb"><div class="frame tone-event" role="img" aria-label="Immagine evento"></div>Lorem ipsum<br>dolor sit amet</div>
  </div>
</section>

<section class="abs box" style="left:126px;top:675px;width:296px;height:116px">
  <div class="box-title">Cinema Lorem Ipsum Dolor Sit Amet</div>
  <div class="arrow" style="left:8px;top:40px"><svg viewBox="0 0 6 9"><path d="M5 0L0 4.5 5 9z" fill="#555"/></svg></div>
  <div class="arrow" style="right:8px;top:40px"><svg viewBox="0 0 6 9"><path d="M1 0l5 4.5L1 9z" fill="#555"/></svg></div>
  <div class="abs thumbs" style="left:36px">
    <div class="thumb"><div class="frame tone-cinema" role="img" aria-label="Locandina film"></div>Lorem ipsum<br>dolor sit amet</div>
    <div class="thumb"><div class="frame tone-cinema" role="img" aria-label="Locandina film"></div>Lorem ipsum<br>dolor sit amet</div>
    <div class="thumb"><div class="frame tone-cinema" role="img" aria-label="Locandina film"></div>Lorem ipsum<br>dolor sit amet</div>
    <div class="thumb"><div class="frame tone-cinema" role="img" aria-label="Locandina film"></div>Lorem ipsum<br>dolor sit amet</div>
  </div>
</section>

<section class="abs box" style="left:126px;top:800px;width:296px;height:116px">
  <div class="box-title">Venues Lorem Ipsum Dolor Sit Amet</div>
  <div class="arrow" style="left:8px;top:40px"><svg viewBox="0 0 6 9"><path d="M5 0L0 4.5 5 9z" fill="#555"/></svg></div>
  <div class="arrow" style="right:8px;top:40px"><svg viewBox="0 0 6 9"><path d="M1 0l5 4.5L1 9z" fill="#555"/></svg></div>
  <div class="abs thumbs" style="left:36px">
    <div class="thumb"><div class="frame tone-venue" role="img" aria-label="Foto del locale"></div>Lorem ipsum<br>dolor sit amet</div>
    <div class="thumb"><div class="frame tone-venue" role="img" aria-label="Foto del locale"></div>Lorem ipsum<br>dolor sit amet</div>
    <div class="thumb"><div class="frame tone-venue" role="img" aria-label="Foto del locale"></div>Lorem ipsum<br>dolor sit amet</div>
    <div class="thumb"><div class="frame tone-venue" role="img" aria-label="Foto del locale"></div>Lorem ipsum<br>dolor sit amet</div>
  </div>
</section>

<section class="abs subscribe" style="top:925px">
  <h3>Ricevere Aggiornamento Settimanale</h3>
  <div class="field"></div>
  <div class="btn-orange">Submit</div>
</section>

<aside class="abs box" style="left:432px;top:183px;width:173px;height:155px;background:var(--panel)">
  <div class="abs map-area" role="img" aria-label="Mappa dell'Italia con i luoghi degli eventi"></div>
  <div class="abs map-tabs"><span>Map</span><span>Satellite</span><span>Hybrid</span></div>
  <div class="abs btn-orange btn-large-map">View Large Map</div>
</aside>

<aside class="abs box" style="left:432px;top:348px;width:173px;height:327px;background:var(--panel)">
  <div style="padding:6px 8px;font-size:7px;color:#555">Find us on Friendwall</div>
  <div class="abs feed-inner" style="height:300px">
    <div class="post"><div class="avatar"></div><div><b>Pellora</b><span style="border:1px solid #bbb;padding:0 3px">Like</span></div></div>
    <div class="post" style="border-top:1px solid #eee"><div class="avatar"></div><div><b>Pellora</b>Nuovi eventi in città questa settimana: concerti, teatro e mostre da non perdere. Scopri tutto sul sito.<br><span style="color:#999">August 11, 2011</span></div></div>
    <div class="post" style="border-top:1px solid #eee"><div class="avatar"></div><div><b>Pellora</b>Aggiornato il calendario del weekend con festival e serate per famiglie in tutta Roma.<br><span style="color:#999">August 9, 2011</span></div></div>
    <div style="padding:4px 5px;font-size:6px;color:#555;border-top:1px solid #eee">People like Pellora</div>
    <div class="fans"><div><div class="face"></div>Sara</div><div><div class="face"></div>Tiziana</div><div><div class="face"></div>Luca</div><div><div class="face"></div>Giorgio</div></div>
    <div style="position:absolute;bottom:4px;left:5px;font-size:5.5px;color:#777">Friendwall social plugin</div>
  </div>
</aside>

<aside class="abs box" style="left:432px;top:692px;width:173px;height:253px;overflow:hidden">
  <div class="news-head">Ultime News</div>
  <div>
    <div class="news-item"><div class="news-date">January 12/2012</div>Lorem ipsum dolor sit amet, consectetur adipis cing elit. Sed diam nonummy gravida neque</div>
    <div class="news-item"><div class="news-date">January 20/2012</div>Lorem ipsum dolor sit amet, consectetur adipis cing elit. Sed diam nonummy gravida neque</div>
    <div class="news-item"><div class="news-date">February 10/2012</div>Lorem ipsum dolor sit amet, consectetur adipis cing elit. Sed diam nonummy gravida neque</div>
    <div class="news-item"><div class="news-date">February 28/2012</div>Lorem ipsum dolor sit amet, consectetur adipis cing elit. Sed diam nonummy gravida neque</div>
    <div class="news-item"><div class="news-date">March 09/2012</div>Lorem ipsum dolor sit amet, consectetur adipis cing elit. Sed diam nonummy gravida neque</div>
  </div>
</aside>

<footer class="abs footer">
  <nav class="abs footer-nav"><span>Home</span><span>Eventi</span><span>Eventi Da Non Perdere</span><span>Catergorie Top</span><span>Luoghi Top</span><span>Film Top</span><span>Contact Us</span></nav>
  <ul class="abs footer-sub"><li>Play</li><li>Altri eventi teatrali</li><li>Mostre d'arte di storia</li><li>Prosa</li><li>Concerts</li><li>Musei e siti archeologici</li></ul>
  <div class="abs footer-rule"></div>
  <div class="abs copyright">Copyright © 2011, Pellora.example. All rights reserved.</div>
</footer>

</body>
</html>
```